BLUE HAVEN (Business Card for Training Company)

Blue Haven is a training and consultancy company with a focus on executive protection and medical. I would like the card to be nice and sharp, not overdone and in black and red. I would also like it to highlight that it is "A Dravin Company"

I would like it to be simple and highlight a few things.

1. Name
2. Title
3. Phone Number
4. Email

I would also like www.dravinholdings.example/blue-haven to be on the card somewhere.

Target Market(s)

Security Companies

Industry/Entity Type

Security

Contact Information for Business Card

Blue Haven is a training and consultancy company with a focus on executive protection and medical. I would like the card to be nice and sharp, not overdone and in black and red. I would also like it to highlight that it is "A Dravin Company" I would like it to be simple and highlight a few things. 1. Name 2. Title 3. Phone Number 4. Email I would also like www.dravinholdings.example/blue-haven to be on the card somewhere.

Requirements
Must have
• A Dravin Company listed on the card and the website
Nice to have
• Highlight Medical Training, Consultancy & Executive Protection Courses

```html
<!DOCTYPE html>
<html lang="en">
<head>
<meta charset="utf-8">
<title>Blue Haven – Business Card Options</title>
<link rel="stylesheet" href="https://fonts.googleapis.com/css2?family=Oswald:wght@500;700&family=Open+Sans:wght@400&display=swap">
<style>
  :root {
    --maroon: #6b0a0a;
    --red: #8e0505;
    --red-dark: #4a0000;
    --accent-red: #e0141b;
    --ink: #111111;
    --band-grey: #d1d2d6;
    --card-light: #ffffff;
    --card-grey: #e4e4e5;
    --page: #ffffff;
  }
  * { box-sizing: border-box; margin: 0; padding: 0; }
  html, body { width: 1200px; height: 1200px; overflow: hidden; background: var(--page); }
  .canvas { position: relative; width: 1200px; height: 1200px; font-family: "Open Sans", Arial, sans-serif; color: var(--ink); }

  .option-label {
    position: absolute; left: 95px;
    font-size: 28px; letter-spacing: 2px; line-height: 1;
  }
  .option-label--one { top: 290px; }
  .option-label--two { top: 878px; }

  .card { position: absolute; left: 281px; width: 831px; height: 499px; overflow: hidden; }
  .card--one { top: 55px; background: linear-gradient(135deg, var(--card-light) 0%, var(--card-grey) 45%, var(--card-light) 100%); }
  .card--two { top: 618px; background: var(--card-light); outline: 1px solid var(--ink); }

  .brand-name {
    position: absolute;
    font-family: "Oswald", Arial, sans-serif; font-weight: 700;
    font-size: 50px; line-height: 0.96; letter-spacing: 1px;
    color: var(--maroon); text-transform: uppercase;
  }
  .card--one .brand-name { left: 47px; top: 46px; }
  .card--two .brand-name { right: 36px; top: 40px; text-align: left; }

  .parent-tag {
    position: absolute;
    font-family: "Oswald", Arial, sans-serif; font-weight: 500;
    color: var(--maroon); text-transform: uppercase; line-height: 1;
  }
  .card--one .parent-tag { right: 49px; top: 48px; font-size: 38px; }
  .card--two .parent-tag { left: 47px; top: 127px; font-size: 32px; }

  .parent-mark { position: absolute; left: 47px; top: 41px; display: flex; align-items: center; gap: 14px; }
  .parent-mark__square { width: 66px; height: 66px; background: var(--maroon); }
  .parent-mark__name {
    font-family: "Oswald", Arial, sans-serif; font-weight: 700;
    font-size: 36px; letter-spacing: 2px; color: var(--ink); text-transform: uppercase;
  }

  .contact { position: absolute; left: 47px; display: flex; align-items: center; font-size: 27px; letter-spacing: 1.5px; line-height: 1; }
  .contact svg { width: 22px; height: 22px; margin-right: 23px; fill: var(--maroon); flex: none; }
  .card--one .contact--phone { top: 204px; }
  .card--one .contact--email { top: 253px; }
  .card--two .contact--phone { top: 232px; }
  .card--two .contact--email { top: 282px; }

  .bands { position: absolute; left: 0; top: 0; width: 831px; height: 499px; }
  .website {
    position: absolute; left: 47px; display: flex; align-items: center;
    font-size: 19px; letter-spacing: 0.5px; line-height: 1; white-space: nowrap;
  }
  .website svg { width: 20px; height: 20px; margin-right: 25px; fill: var(--maroon); flex: none; }
  .card--one .website { top: 360px; }
  .card--two .website { top: 359px; }

  .services {
    position: absolute; left: 0; width: 831px; height: 61px;
    display: flex; align-items: center; justify-content: center; gap: 14px;
    font-family: "Oswald", Arial, sans-serif; font-weight: 500;
    font-size: 26px; color: #ffffff; text-transform: uppercase; letter-spacing: -0.2px;
  }
  .card--one .services { top: 400px; }
  .card--two .services { top: 399px; }
  .services__divider { width: 3px; height: 29px; background: var(--accent-red); }
</style>
</head>
<body>
<main class="canvas">

  <p class="option-label option-label--one">OPTION #1</p>
  <section class="card card--one" aria-label="Business card option one">
    <svg class="bands" viewBox="0 0 831 499" aria-hidden="true">
      <polygon points="0,343 519,343 544,400 0,400" fill="var(--band-grey)"/>
      <polygon points="497,343 510,324 519,343" fill="var(--red-dark)"/>
      <polygon points="510,324 831,324 831,400 544,400" fill="var(--red)"/>
      <rect x="0" y="400" width="831" height="61" fill="var(--ink)"/>
      <rect x="0" y="461" width="831" height="38" fill="var(--band-grey)"/>
    </svg>
    <h1 class="brand-name">Blue<br>Haven</h1>
    <p class="parent-tag">A Dravin Company</p>
    <p class="contact contact--phone">
      <svg viewBox="0 0 24 24"><path d="M6.6 2.5l3 3.6-1.9 2.3c1.2 2.6 3.3 4.8 5.9 6l2.3-1.9 3.6 3-1.6 3.2c-.4.7-1.2 1.1-2 .9C9.4 18.3 5.7 14.6 3.4 8.1c-.2-.8.2-1.6.9-2z"/></svg>
      +000 1234 5678 999
    </p>
    <p class="contact contact--email">
      <svg viewBox="0 0 24 24"><path d="M1 5h22v15H1z M2.5 6.5l9.5 7 9.5-7v-.2H2.5z M2.5 18.5h19l-7-6-2.5 2-2.5-2z" fill-rule="evenodd"/></svg>
      info@dravinholdings.example
    </p>
    <p class="website">
      <svg viewBox="0 0 24 24"><circle cx="4" cy="20" r="2.5"/><path d="M2 11a11 11 0 0 1 11 11h-2.5A8.5 8.5 0 0 0 2 13.5z M2 5a17 17 0 0 1 17 17h-2.5A14.5 14.5 0 0 0 2 7.5z"/></svg>
      www.dravinholdings.example/blue-haven
    </p>
    <div class="services">
      <span>Medical Training</span><span class="services__divider"></span>
      <span>Consultancy</span><span class="services__divider"></span>
      <span>Executive Protection Courses</span>
    </div>
  </section>

  <p class="option-label option-label--two">OPTION #2</p>
  <section class="card card--two" aria-label="Business card option two">
    <svg class="bands" viewBox="0 0 831 499" aria-hidden="true">
      <polygon points="0,342 519,342 544,399 0,399" fill="var(--band-grey)"/>
      <polygon points="497,342 510,323 519,342" fill="var(--red-dark)"/>
      <polygon points="510,323 831,323 831,399 544,399" fill="var(--red)"/>
      <rect x="0" y="399" width="831" height="61" fill="var(--ink)"/>
      <rect x="0" y="460" width="831" height="39" fill="var(--band-grey)"/>
    </svg>
    <div class="parent-mark">
      <span class="parent-mark__square"></span>
      <span class="parent-mark__name">Dravin Group</span>
    </div>
    <p class="parent-tag">A Dravin Company</p>
    <h1 class="brand-name">Blue<br>Haven</h1>
    <p class="contact contact--phone">
      <svg viewBox="0 0 24 24"><path d="M6.6 2.5l3 3.6-1.9 2.3c1.2 2.6 3.3 4.8 5.9 6l2.3-1.9 3.6 3-1.6 3.2c-.4.7-1.2 1.1-2 .9C9.4 18.3 5.7 14.6 3.4 8.1c-.2-.8.2-1.6.9-2z"/></svg>
      +000 1234 5678 999
    </p>
    <p class="contact contact--email">
      <svg viewBox="0 0 24 24"><path d="M1 5h22v15H1z M2.5 6.5l9.5 7 9.5-7v-.2H2.5z M2.5 18.5h19l-7-6-2.5 2-2.5-2z" fill-rule="evenodd"/></svg>
      info@dravinholdings.example
    </p>
    <p class="website">
      <svg viewBox="0 0 24 24"><circle cx="4" cy="20" r="2.5"/><path d="M2 11a11 11 0 0 1 11 11h-2.5A8.5 8.5 0 0 0 2 13.5z M2 5a17 17 0 0 1 17 17h-2.5A14.5 14.5 0 0 0 2 7.5z"/></svg>
      www.dravinholdings.example/blue-haven
    </p>
    <div class="services">
      <span>Medical Training</span><span class="services__divider"></span>
      <span>Consultancy</span><span class="services__divider"></span>
      <span>Executive Protection Courses</span>
    </div>
  </section>

</main>
</body>
</html>
```